Website Design Idea Only

I need a WordPress compatible website design idea. I have already hired a programmer, however; I am not happy with the design ideas he has come up with, I need help in creating a professional but classy/unique design for my company website.

A bit about my company....
Bid Compass (the logo was created here on ArtHive and I love it!!) is a brokerage company... I source out Print, Design and Websites for my customers, helping them find the best quality for the best prices, and saving them time and money by managing the project.
My company was called "M.R.K. Design & Printing", and you can view the current site at mrkdesign-printing.example, but I am now operating as Bid Compass so I am needing an updated site.

What I would like to see in the site...
Because my site will be a big selling feature, I would like it to be professional, but some really nice/creative design characteristics to it. I am attaching what my programmer has come up with and you'll see it is very flat, and the pictures way to large. "Bid Compass-updated.jpg"
I am also attaching my logo, and a couple of site ideas I found that I like as well.

I was hoping for some sort of wave at the top, or something eye catching.
The design should say we are professional, but are creative and classy.
I love the gold/brown combination, as that is my logo, but I don't want a totally dark background, I like the use of whitespace as well.

Please feel free to contact my anytime if you have any questions, I will be happy to help!
Norma
norma@bidcompass.example

Please note: This design will proceed the design of two or three trade show pull up banners, which I am wanting to award to the winning designer. Please keep in mind that the graphics will need to be available in a vector format to accommodate that.

Thank you!!

Target Market(s)

Business to business - small to medium sized business.

Number of Pages Required

3 page

Requirements
Must have
• Please design a home page, a landing page that is specific to 'printing' or 'websites', as well as a 'regular' page.

```html
<!DOCTYPE html>
<html lang="en">
<head>
<meta charset="utf-8">
<title>Bid Compass – Printing Brokerage</title>
<link href="https://fonts.googleapis.com/css2?family=Cinzel:wght@400;700&family=PT+Sans:wght@400;700&family=Crimson+Text:ital@1&display=swap" rel="stylesheet">
<style>
:root{
  --brown-dark:#231309;
  --brown:#2e1a0c;
  --gold:#c8842a;
  --gold-light:#e6c06a;
  --gold-soft:#d9a64a;
  --ink:#222;
  --grey-band:#f1f1f1;
  --white:#fff;
}
*{margin:0;padding:0;box-sizing:border-box}
html,body{width:772px;height:1200px;overflow:hidden;background:var(--white)}
body{position:relative;font-family:"PT Sans",sans-serif;color:var(--ink)}
.abs{position:absolute}

.top-bar{left:0;top:0;width:772px;height:65px;background:var(--brown-dark)}
.top-bar::before{content:"";position:absolute;left:0;top:0;width:100%;height:5px;
  background:linear-gradient(135deg,var(--white) 25%,transparent 25%) 0 0/8px 8px,
             linear-gradient(225deg,var(--white) 25%,transparent 25%) 0 0/8px 8px}
.call-line{right:112px;top:17px;font-family:"Crimson Text",serif;font-style:italic;font-size:9px;color:#eee;text-align:right}
.call-phone{right:112px;top:29px;font-size:15px;font-weight:700;color:var(--gold-soft);letter-spacing:.5px}
.social{top:20px;width:24px;height:24px;background:#3a2414}
.social.one{left:670px}.social.two{left:700px}

.nav-bar{left:0;top:65px;width:772px;height:29px;background:linear-gradient(180deg,#f0d27e,#c99a3f)}
.nav{left:232px;top:65px;height:29px;display:flex;list-style:none}
.nav li{font-size:9.5px;color:var(--brown);line-height:29px;padding:0 16px;text-transform:uppercase}
.nav li.active{background:var(--gold);color:var(--white);padding:0 14px}

.logo-box{left:49px;top:0;width:140px;height:104px;background:var(--brown-dark);box-shadow:0 3px 6px rgba(0,0,0,.5);text-align:center;z-index:3}
.logo-mark{width:30px;height:30px;border-radius:50%;border:3px solid var(--gold-soft);margin:14px auto 6px}
.logo-name{font-family:"Cinzel",serif;font-size:15px;color:var(--gold-soft);letter-spacing:.5px}
.logo-tag{font-family:"Crimson Text",serif;font-style:italic;font-size:7px;color:#ddd;margin-top:1px}

.hero{left:0;top:94px;width:772px;height:268px;background:linear-gradient(135deg,#3a3633,#1f1d1b 55%,#2d2a27)}
.hero-title{left:163px;top:197px;width:445px;height:30px;background:#150c05;color:var(--white);font-family:"Cinzel",serif;font-size:18px;text-align:center;line-height:30px;letter-spacing:.5px}
.hero-sub{left:145px;top:232px;width:481px;height:30px;background:var(--gold);color:var(--white);font-family:"Cinzel",serif;font-size:13px;text-align:center;line-height:30px;letter-spacing:.5px}

.testimonial{left:0;top:362px;width:772px;height:83px;background:var(--grey-band)}
.avatar{left:47px;top:379px;width:48px;height:48px;border-radius:50%;background:linear-gradient(#c9b6a4,#2b2b33);border:2px solid var(--white);box-shadow:0 1px 3px rgba(0,0,0,.3)}
.quote{left:111px;top:381px;width:620px;font-family:"Crimson Text",serif;font-style:italic;font-size:10.5px;line-height:15.5px;color:#222}
.quote b{font-weight:700}

.intro{left:40px;top:472px;width:692px;text-align:center}
.intro-lead{font-size:15.5px;line-height:22px;color:#222}
.intro-lead em{font-style:normal;font-weight:700;color:var(--gold)}
.intro-body{font-size:11px;line-height:18px;margin-top:10px;color:#333}

.divider{left:0;top:580px}

.services-title{left:0;top:648px;width:772px;text-align:center;font-family:"Cinzel",serif;font-size:26px;color:#3a3a3a;letter-spacing:1px}
.services-title span{color:var(--gold)}
.service{top:705px;width:150px;text-align:center}
.service svg{display:block;margin:0 auto}
.service-label{font-size:11.5px;margin-top:14px;text-transform:uppercase;color:#222}
.connectors{left:0;top:830px}

.quote-band{left:0;top:917px;width:772px;height:237px;background:radial-gradient(ellipse at 60% 40%,#6b3e14,#3c220b 70%,#2a1707)}
.quote-title{left:0;top:975px;width:772px;text-align:center;font-family:"Cinzel",serif;font-size:26px;color:var(--white);letter-spacing:1px}
.field{top:1040px;height:33px;background:var(--white);border:1px solid var(--gold);font-size:11.5px;color:#222;line-height:31px;padding-left:12px;text-transform:uppercase}
.field.email{left:88px;width:249px}
.field.category{left:349px;width:213px}
.field.category svg{position:absolute;right:10px;top:11px}
.submit{left:575px;top:1040px;width:109px;height:33px;background:linear-gradient(180deg,#e2b862,#c38a35);color:var(--brown);font-size:12px;text-align:center;line-height:33px;text-transform:uppercase}

.footer{left:0;top:1170px;width:772px;text-align:center;font-size:8px;color:#333}
.footer span{color:var(--gold);font-weight:700}
</style>
</head>
<body>
<header>
  <div class="abs top-bar"></div>
  <div class="abs call-line">Give us a call to start saving time and money today!</div>
  <div class="abs call-phone">1-888-555-0142</div>
  <div class="abs social one" aria-label="Social profile"></div>
  <div class="abs social two" aria-label="Social profile"></div>
  <div class="abs nav-bar"></div>
  <ul class="abs nav">
    <li class="active">Home</li><li>About Us</li><li>Resources</li><li>Request a Quote</li><li>Our Monthly Deal</li><li>Contact Us</li>
  </ul>
  <div class="abs logo-box">
    <div class="logo-mark"></div>
    <div class="logo-name">BID COMPASS</div>
    <div class="logo-tag">The Smart Way to Save Money</div>
  </div>
</header>

<section>
  <div class="abs hero" role="img" aria-label="Photo of printed stationery and business cards on a dark wooden desk"></div>
  <h1 class="abs hero-title">ALBERTA’S PREMIERE PRINTING BROKERAGE</h1>
  <h2 class="abs hero-sub">SAVING TIME AND MONEY ON ALL YOUR PRINTING AND DESIGN</h2>
</section>

<section>
  <div class="abs testimonial"></div>
  <div class="abs avatar" role="img" aria-label="Portrait photo of a client"></div>
  <p class="abs quote">Lorem ipsum dolor sit amet, consectetur adipiscing elit, sed do eiusmod tempor incididunt ut labore et dolore magna aliqua. Lorem ipsum dolor sit amet, consectetur adipiscing elit, sed do eiusmod tempor incididunt ut labore et dolore magna aliqua.<br><b>-Darren-</b></p>
</section>

<section class="abs intro">
  <p class="intro-lead">We feel every project is important and <em>the lowest price</em> and <em>the best quality</em> are just the starting points for our relationship. We’ll show you just what a professional brokerage can do for you!</p>
  <p class="intro-body">We take time to understand our customer’s true needs, and we do whatever it takes to meet, and often exceed their expectations. It’s the personal relationship that we have developed that set Bid Compass.</p>
</section>

<svg class="abs divider" width="772" height="50" viewBox="0 0 772 50">
  <polyline points="0,3 386,38 772,3" fill="none" stroke="#e6e6e6" stroke-width="4"/>
</svg>

<h2 class="abs services-title">OUR <span>SERVICES</span></h2>

<div class="abs service" style="left:51px">
  <svg width="50" height="84" viewBox="0 0 50 84" fill="#c8842a">
    <path d="M6 12 L40 0 L40 64 L6 76 Z"/>
    <path d="M2 16 L6 14 L6 80 L36 70 L40 74 L6 84 L2 80 Z"/>
    <path d="M40 64 L46 60 L46 8 L40 6 Z" fill="#a96a1d"/>
    <path d="M12 22 L32 15 M12 28 L32 21" stroke="#fff" stroke-width="2"/>
    <path d="M36 66 L36 82 L40 78 L44 82 L44 64 Z" fill="#a96a1d"/>
  </svg>
  <div class="service-label">Book and Magazine</div>
</div>
<div class="abs service" style="left:223px">
  <svg width="90" height="84" viewBox="0 0 90 84" fill="#c8842a">
    <rect x="2" y="14" width="86" height="58" rx="2"/>
    <rect x="9" y="21" width="72" height="44" fill="#fff"/>
    <rect x="38" y="72" width="14" height="6"/><rect x="28" y="78" width="34" height="5"/>
    <path d="M82 0 L88 4 L56 46 L50 42 Z"/>
    <path d="M50 42 L56 46 C52 54 44 56 38 54 C44 50 46 46 50 42 Z"/>
  </svg>
  <div class="service-label">Book and Magazine</div>
</div>
<div class="abs service" style="left:398px">
  <svg width="88" height="84" viewBox="0 0 88 84" fill="#c8842a">
    <path d="M2 30 L44 2 L86 30 L86 84 L2 84 Z"/>
    <path d="M8 36 L44 60 L80 36 L80 79 L8 79 Z" fill="#fff"/>
    <path d="M8 79 L40 56 L44 60 L48 56 L80 79 Z" fill="#c8842a"/>
    <path d="M12 79 L40 60 L44 63 L48 60 L76 79 Z" fill="#fff"/>
    <text x="44" y="38" text-anchor="middle" font-family="PT Sans,sans-serif" font-weight="700" font-size="26" fill="#fff">@</text>
  </svg>
  <div class="service-label">Mailing Services</div>
</div>
<div class="abs service" style="left:571px">
  <svg width="94" height="84" viewBox="0 0 94 84" fill="#c8842a">
    <path d="M24 0 L58 0 L70 12 L70 30 L24 30 Z"/>
    <path d="M58 0 L58 12 L70 12 Z" fill="#fff"/>
    <rect x="0" y="28" width="94" height="26" rx="2"/>
    <rect x="6" y="36" width="10" height="4" fill="#fff"/>
    <rect x="20" y="54" width="54" height="26" fill="#fff" stroke="#c8842a" stroke-width="5"/>
    <rect x="8" y="54" width="8" height="26"/><rect x="78" y="54" width="8" height="26"/>
    <rect x="4" y="78" width="86" height="6"/>
  </svg>
  <div class="service-label">Large Format</div>
</div>

<svg class="abs connectors" width="772" height="120" viewBox="0 0 772 120" fill="none" stroke="#c8842a" stroke-width="2.4" stroke-linecap="round" stroke-dasharray="0 6.5">
  <path d="M126 3 V31 M298 3 V31 M473 3 V31 M646 3 V31"/>
  <path d="M126 31 H646"/>
  <path d="M386 35 V120"/>
</svg>

<section>
  <div class="abs quote-band" role="img" aria-label="Warm brown photo of hands at a keyboard reviewing printed charts"></div>
  <svg class="abs" style="left:370px;top:917px" width="32" height="40" viewBox="0 0 32 40" fill="none" stroke="#fff" stroke-width="2.4" stroke-linecap="round" stroke-dasharray="0 6.5">
    <path d="M16 2 V30"/><path d="M6 24 L16 34 L26 24"/>
  </svg>
  <h2 class="abs quote-title">REQUEST A QUOTE</h2>
  <div class="abs field email">Your E-mail</div>
  <div class="abs field category">Category
    <svg width="12" height="10" viewBox="0 0 12 10" fill="none" stroke="#c8842a" stroke-width="1.5"><path d="M1 1 L6 5 L11 1 M1 5 L6 9 L11 5"/></svg>
  </div>
  <div class="abs submit">Submit</div>
</section>

<footer class="abs footer">(c) 2014 <span>BidCompass.example</span> . All rights reserved.</footer>
</body>
</html>
```